Hot Offer banner for product listing page

Hi, we need a banner in the dimensions 210x390px which will be shown in the product listing on our online shop. There are 18 products and in between randomly there should be 3 banners with three different information.
first banner: fast delivery
The idea is to show a stove which is very "fast". Maybe you can make an effect like in Driftcraft Valorne when they activate the warp drive or something similar. Anyway, the banner should indicate that the delivery is very fast for this product.

second banner: Advantage banner
We would like to have a banner which names all our advantages in our online shop. this is the list of advantages:
- over 200,000 satisfied customers
- Best price guarantee
- thousands of devices in stock
- Top ratings

I attached you some examples, just to give you an idea.

```html
<!DOCTYPE html>
<html lang="en">
<head>
<meta charset="utf-8">
<title>Shop Banners – Fast Delivery &amp; Advantages</title>
<link rel="stylesheet" href="https://fonts.googleapis.com/css2?family=Roboto:wght@400;700&display=swap">
<style>
  :root {
    --canvas-bg: #e8e5e5;
    --brand-orange: #f28c00;
    --orange-light: #f9a21c;
    --cream: #f6e2c4;
    --cream-soft: #f3d3a2;
    --charcoal: #4a4645;
    --white: #ffffff;
    --stove-dark: #2e3134;
  }
  * { box-sizing: border-box; margin: 0; padding: 0; }
  html, body { width: 1200px; height: 1039px; overflow: hidden; }
  body {
    background: var(--canvas-bg);
    font-family: "Roboto", Arial, sans-serif;
    position: relative;
  }
  .banner {
    position: absolute;
    top: 136px;
    width: 352px;
    height: 654px;
    background: var(--brand-orange);
    overflow: hidden;
    box-shadow: 0 2px 6px rgba(0,0,0,0.25);
  }
  .banner--delivery { left: 188px; }
  .banner--advantages { left: 645px; }

  /* Fast delivery banner */
  .delivery-icon {
    position: absolute;
    left: 108px; top: 28px;
    width: 136px; height: 64px;
  }
  .delivery-title {
    position: absolute;
    top: 100px; left: 0; width: 100%;
    text-align: center;
    color: var(--white);
    font-weight: 500;
    font-size: 27px;
    letter-spacing: 0.3px;
  }
  .delivery-visual {
    position: absolute;
    left: 0; top: 150px;
    width: 100%; height: 504px;
    background:
      radial-gradient(ellipse 30% 48% at 50% 48%, var(--stove-dark) 0 92%, transparent 100%),
      radial-gradient(ellipse 90% 40% at 50% 95%, #f7f1e6 0%, rgba(240,120,60,0.6) 45%, transparent 80%),
      linear-gradient(180deg, var(--brand-orange) 0%, var(--orange-light) 55%, #e9662a 100%);
  }

  /* Advantages banner */
  .advantage {
    position: absolute;
    left: 0;
    width: 100%;
    height: 156px;
  }
  .advantage__halo {
    position: absolute;
    left: -100px; top: -2px;
    width: 180px; height: 160px;
    border-radius: 50%;
    background: radial-gradient(circle at 60% 50%, var(--cream) 0%, var(--cream-soft) 70%, rgba(243,211,162,0.3) 100%);
  }
  .advantage__badge {
    position: absolute;
    left: 11px; top: 30px;
    width: 96px; height: 96px;
    border-radius: 50%;
    background: var(--charcoal);
    display: flex; align-items: center; justify-content: center;
  }
  .advantage__badge svg { width: 56px; height: 56px; }
  .advantage__text {
    position: absolute;
    left: 122px; top: 50%;
    transform: translateY(-50%);
    color: var(--white);
    font-size: 23px;
    line-height: 1.3;
    text-transform: uppercase;
    font-weight: 400;
  }
  .advantage__text strong { font-weight: 700; }
</style>
</head>
<body>

  <section class="banner banner--delivery">
    <svg class="delivery-icon" viewBox="0 0 136 64" fill="none" stroke="#ffffff" stroke-width="5" stroke-linejoin="round" stroke-linecap="round" aria-hidden="true">
      <line x1="4" y1="14" x2="34" y2="14"/>
      <line x1="0" y1="26" x2="28" y2="26"/>
      <line x1="8" y1="38" x2="30" y2="38"/>
      <path d="M40 6 H96 V48 H40 Z"/>
      <path d="M96 20 H116 L130 36 V48 H96"/>
      <circle cx="56" cy="52" r="8" fill="#f28c00"/>
      <circle cx="114" cy="52" r="8" fill="#f28c00"/>
    </svg>
    <h2 class="delivery-title">FAST DELIVERY</h2>
    <div class="delivery-visual" role="img" aria-label="Black round wood-burning stove with visible fire, speeding forward over warp-speed light streaks"></div>
  </section>

  <section class="banner banner--advantages">
    <div class="advantage" style="top: 10px;">
      <div class="advantage__halo"></div>
      <div class="advantage__badge">
        <svg viewBox="0 0 56 56" fill="none" stroke="#f28c00" stroke-width="6" stroke-linecap="round" stroke-linejoin="round" aria-hidden="true">
          <path d="M12 29 L24 41 L45 16"/>
        </svg>
      </div>
      <p class="advantage__text">Over 200,000<br><strong>Satisfied<br>Customers</strong></p>
    </div>

    <div class="advantage" style="top: 166px;">
      <div class="advantage__halo"></div>
      <div class="advantage__badge">
        <svg viewBox="0 0 56 56" fill="none" stroke="#f28c00" stroke-width="4" stroke-linejoin="round" aria-hidden="true">
          <path d="M8 8 H26 L50 32 L32 50 L8 26 Z"/>
          <circle cx="18" cy="18" r="3.5"/>
        </svg>
      </div>
      <p class="advantage__text"><strong>Best Price</strong><br>Guarantee</p>
    </div>

    <div class="advantage" style="top: 322px;">
      <div class="advantage__halo"></div>
      <div class="advantage__badge">
        <svg viewBox="0 0 56 56" fill="#f28c00" aria-hidden="true">
          <rect x="22" y="6" width="12" height="12"/>
          <rect x="14" y="20" width="12" height="12"/>
          <rect x="30" y="20" width="12" height="12"/>
          <rect x="6" y="34" width="12" height="12"/>
          <rect x="22" y="34" width="12" height="12"/>
          <rect x="38" y="34" width="12" height="12"/>
        </svg>
      </div>
      <p class="advantage__text"><strong>Thousands of<br>Devices</strong> in Stock</p>
    </div>

    <div class="advantage" style="top: 478px;">
      <div class="advantage__halo"></div>
      <div class="advantage__badge">
        <svg viewBox="0 0 70 14" fill="#f28c00" aria-hidden="true" style="width:70px;height:14px;">
          <g id="star"><polygon points="7,0 8.7,4.8 13.7,4.9 9.7,8 11.1,12.9 7,10 2.9,12.9 4.3,8 0.3,4.9 5.3,4.8"/></g>
          <use href="#star" x="14"/>
          <use href="#star" x="28"/>
          <use href="#star" x="42"/>
          <use href="#star" x="56"/>
        </svg>
      </div>
      <p class="advantage__text"><strong>Top Ratings</strong></p>
    </div>
  </section>

</body>
</html>
```